Consultant ot credit unions that operate a property and casualty insurance agency

Industry/Entity Type

Insurance

Contact Information for Business Card

Dorian Velcote
Tidewell Agency Group Agency Consultant
dorianvelcote@mailbrook.example
562 318-4092
418 Tamsin Court
Long Beach, CA 90814

```html
<!DOCTYPE html>
<html lang="en">
<head>
<meta charset="utf-8">
<title>Dorian Velcote – Business Card</title>
<link rel="stylesheet" href="https://fonts.googleapis.com/css2?family=Tinos:wght@700&family=Arimo:wght@400&display=swap">
<style>
  :root {
    --navy: #2b2a7c;
    --paper: #fdfdfd;
    --backdrop: #ececee;
    --white: #ffffff;
  }
  * { box-sizing: border-box; margin: 0; padding: 0; }
  html, body {
    width: 1200px;
    height: 864px;
    overflow: hidden;
    background: var(--backdrop);
  }
  .canvas {
    position: relative;
    width: 1200px;
    height: 864px;
  }
  .card {
    position: absolute;
    left: 75px;
    top: 132px;
    width: 1050px;
    height: 600px;
    background: var(--paper);
    color: var(--navy);
    box-shadow: 0 6px 24px rgba(0,0,0,0.12);
    overflow: hidden;
  }
  .agency-name {
    position: absolute;
    left: 70px;
    top: 232px;
    width: 380px;
    text-align: center;
    font-family: "Arimo", Arial, sans-serif;
    font-size: 44px;
    line-height: 1.05;
    font-weight: 400;
    color: var(--navy);
  }
  .divider {
    position: absolute;
    left: 476px;
    top: 60px;
    width: 2px;
    height: 390px;
    background: var(--navy);
  }
  .identity {
    position: absolute;
    left: 590px;
    top: 80px;
  }
  .identity .person {
    font-family: "Tinos", "Times New Roman", serif;
    font-weight: 700;
    font-size: 32px;
    line-height: 1;
  }
  .identity .role {
    font-family: "Arimo", Arial, sans-serif;
    font-size: 20px;
    line-height: 1.1;
    margin-top: 2px;
  }
  .contacts {
    position: absolute;
    left: 618px;
    top: 350px;
    list-style: none;
    font-family: "Arimo", Arial, sans-serif;
    font-size: 21px;
  }
  .contacts li {
    display: flex;
    align-items: center;
    gap: 14px;
    height: 34px;
  }
  .contacts svg { width: 20px; height: 20px; fill: var(--navy); flex: none; }
  .address-band {
    position: absolute;
    left: 0;
    bottom: 0;
    width: 100%;
    height: 62px;
    background: var(--navy);
    color: var(--white);
    font-family: "Arimo", Arial, sans-serif;
    font-size: 28px;
    display: flex;
    align-items: center;
    justify-content: center;
    padding-left: 60px;
  }
</style>
</head>
<body>
<main class="canvas">
  <article class="card">
    <h1 class="agency-name">Tidewell<br>Agency Group</h1>
    <div class="divider"></div>
    <div class="identity">
      <p class="person">Dorian Velcote</p>
      <p class="role">Agency Consultant</p>
    </div>
    <ul class="contacts">
      <li>
        <svg viewBox="0 0 24 24" aria-hidden="true"><path d="M6.6 10.8a15.2 15.2 0 0 0 6.6 6.6l2.2-2.2a1 1 0 0 1 1-.25 11.4 11.4 0 0 0 3.6.57 1 1 0 0 1 1 1V20a1 1 0 0 1-1 1A17 17 0 0 1 3 4a1 1 0 0 1 1-1h3.5a1 1 0 0 1 1 1c0 1.25.2 2.45.57 3.57a1 1 0 0 1-.25 1z"/></svg>
        <span>562 318-4092</span>
      </li>
      <li>
        <svg viewBox="0 0 24 24" aria-hidden="true"><path d="M2 5h20L12 12.5zM2 7l10 7.5L22 7v12H2z"/></svg>
        <span>dorianvelcote@mailbrook.example</span>
      </li>
    </ul>
    <footer class="address-band">418 Tamsin Court Long Beach, CA 90814</footer>
  </article>
</main>
</body>
</html>
```